Lou Benfield Tennis Academy - New Website

Our business is built around classes for all ages, competitions, and court hire.

There are a few gym style Wordpress templates that I think will have most of the functionality we need, but we don't like the style. We are looking for someone to make us a design that can be implemented as a child theme to one of these gym based Wordpress themes.

We have looked at:

http://stylebazaar.net/item/active-hall-responsive-wordpress-theme/full_screen_preview/7381926?ref=PixDepot
http://www.zulu-layouts.com/item/gym-fitness/demo/?r=pixdepot
http://www.pribo.tf/redirect/?theme=movenow

For style we are looking for something fresh, clean, and vibrant. Our logo is teal and gold with some red, orange, green and yellow.

https://huetray.examplehub.com/Mineral-D-color-theme-837465/
https://huetray.examplehub.com/Lozenge-D-color-theme-619372/
https://huetray.examplehub.com/Palermo-color-theme-57031/

These are the colour schemes we are leaning towards.

Our current website can be seen here www.lbta.com.au
Updates

The new logo design will be uploaded shortly. We don't need any more work done on that.

A rough logo file has been added for you to work with.

Could I please get some submissions that include what the other pages on the website will look like (instead of just the home page).

I think it's really important that we get the look of the product page. See the design pdf for our ideas on the layout of those pages.

***Edit*** Single product pages, I mean. I think the "Classes" page itself will be based a lot on the theme used so I'm less concerned about that. I just want to see what a page will look like that is only for.... Social Tennis (for example)

Target Market(s)

We teach a lot of kids but also many comp players. Everything needs to be very clear and easy to navigate.

Industry/Entity Type

Court

Requirements
Must have
• Custom content types to easily post new things (eg, new programs, new coaches)
Timetable page that is dynamic based on the programs custom type.
Programs page that is dynamic based on the programs custom type.
Coaches page that is dynamic based on the coaches/trainers content type.

Page templates for programs, competitions and a few other things as per pdf.

```html
<!DOCTYPE html>
<html lang="en">
<head>
<meta charset="utf-8">
<title>Lou Benfield Tennis Academy</title>
<link rel="stylesheet" href="https://fonts.googleapis.com/css2?family=Open+Sans:wght@300;400;600;700&family=Bree+Serif&family=Kaushan+Script&family=Oswald:wght@400;500&display=swap">
<style>
:root{
  --teal:#2ea6b3;
  --logo-teal:#1e9bb0;
  --cream:#fdf0dc;
  --orange:#f26d0c;
  --yellow:#f7b52b;
  --brick:#a4412a;
  --grey-bg:#f2f2f2;
  --card-border:#9a9a9a;
  --text:#222;
}
*{box-sizing:border-box;margin:0;padding:0}
html,body{width:959px;height:1200px;overflow:hidden}
body{position:relative;background:#fff;font-family:"Open Sans",Arial,sans-serif;color:var(--text)}
.abs{position:absolute}

.site-header{position:absolute;left:0;top:0;width:959px;height:167px;background:var(--cream);border-top:3px solid var(--teal)}
.brand{position:absolute;left:120px;top:26px;display:flex;align-items:center;gap:10px;font-weight:700;color:var(--logo-teal);font-size:24px;line-height:27px;letter-spacing:.5px}
.brand-dot{width:14px;height:14px;border-radius:50%;background:var(--logo-teal)}
.top-links{position:absolute;left:632px;top:42px;font-size:12.5px;color:#333;display:flex;gap:12px}
.social{position:absolute;top:40px;width:26px;height:26px;border-radius:50%;background:#2390c0}

.main-nav{position:absolute;left:120px;top:106px;width:719px;height:47px;background:linear-gradient(#f7841c,#e8600a);border-radius:5px;box-shadow:0 2px 3px rgba(0,0,0,.2)}
.main-nav ul{position:absolute;left:7px;top:7px;width:705px;height:33px;list-style:none;display:flex;background:linear-gradient(#fff,#e8e8e8);border-radius:3px}
.main-nav li{height:33px;line-height:33px;font-size:13px;color:#222;text-align:center;border-right:1px solid #ccc}
.main-nav li:last-child{border-right:none}

.hero{position:absolute;left:0;top:167px;width:959px;height:370px;
  background:
    linear-gradient(180deg,rgba(0,0,0,0) 0%,rgba(0,0,0,0) 56%,rgba(40,60,20,.35) 60%,rgba(0,0,0,0) 72%),
    linear-gradient(180deg,#2f3a26 0%,#3d4a2f 40%,#44512f 57%,#5f7d3a 62%,#6c8c45 70%,#7ea062 74%,#88a96c 100%);}
.who{position:absolute;left:667px;top:367px;width:164px;height:170px;background:rgba(255,255,255,.9);text-align:center;padding:6px 10px}
.who h2{font-weight:300;font-size:21px;color:var(--teal);margin-bottom:5px}
.who p{font-size:9.6px;line-height:15px;color:#8a8a8a}
.who-arrows{position:absolute;left:667px;top:537px;width:164px;height:24px;display:flex}
.who-arrows div{flex:1;display:flex;align-items:center;justify-content:center}

.camp-banner{position:absolute;left:127px;top:576px;width:704px;height:113px;background:var(--brick);overflow:hidden}
.camp-banner .dash{position:absolute;left:6px;top:6px;right:6px;bottom:6px;border:1px dashed rgba(255,220,190,.45)}
.camp-photo{position:absolute;left:345px;top:0;width:150px;height:113px;background:linear-gradient(90deg,rgba(164,65,42,0),#b85a3c 25%,#9c4a3a 75%,rgba(164,65,42,0))}
.camp-title{position:absolute;left:24px;top:24px;font-family:"Kaushan Script",cursive;font-size:31px;color:#f9b233;white-space:nowrap}
.camp-sub{position:absolute;left:97px;top:68px;font-size:14px;color:#fff}
.book-btn{position:absolute;left:537px;top:42px;width:135px;height:29px;border-radius:4px;background:linear-gradient(#f78a2c,#e0580a);border:1px solid #c24d08;color:#fff;font-family:"Oswald",sans-serif;font-size:14px;line-height:27px;text-align:center}
.dots{position:absolute;left:458px;top:699px;display:flex;gap:4px}
.dots span{width:5px;height:5px;border-radius:50%;background:#ccc}
.dots span:first-child{background:#8fd0dc}

.widgets{position:absolute;left:0;top:727px;width:959px;height:345px;background:var(--grey-bg)}
.card{position:absolute;top:24px;width:224px;height:281px;background:#fff;border:3px solid var(--card-border);border-radius:5px;box-shadow:0 3px 4px rgba(0,0,0,.15)}
.card-title{position:absolute;left:9px;top:9px;width:202px;height:39px;border-radius:3px;background:linear-gradient(#fbb02c,#f28b12);font-family:"Bree Serif",serif;color:#fff;font-size:20px;line-height:39px;padding-left:11px}
.learn{position:absolute;left:66px;bottom:-13px;width:88px;height:30px;background:linear-gradient(#f57c1e,#e25b0b);border:3px solid #c9c9c9;border-radius:4px;color:#fff;font-size:10.5px;font-weight:600;text-align:center;line-height:24px}
.player-photo{position:absolute;left:12px;top:66px;width:196px;height:134px;border:3px solid #e6e6e6;background:linear-gradient(135deg,#d9c7a5,#7a8fa8 55%,#4a5f86)}
.player-name{position:absolute;left:16px;top:206px;font-family:"Oswald",sans-serif;font-weight:500;font-size:17.5px;color:#222}
.post{position:absolute;left:9px;width:204px}
.post h3{font-size:11.5px;font-weight:600}
.post .meta{font-size:8px;color:#999}
.post .meta b{color:var(--orange);font-weight:400}
.post .thumb{position:absolute;left:0;top:36px;width:52px;height:52px;border:1px solid #ddd;background:linear-gradient(#eef6fb,#cfe6f2)}
.post p{position:absolute;left:63px;top:32px;width:140px;font-size:9.4px;line-height:12.5px;color:#666}
.post p b{color:var(--orange);font-weight:400}
.event{position:absolute;left:9px;width:204px;height:64px;border-bottom:1px solid #e5e5e5}
.badge{position:absolute;left:3px;top:0;width:42px;height:42px;border-radius:50%;background:var(--teal);border:3px solid #d7eef1;color:#fff;text-align:center;font-weight:700}
.badge small{display:block;font-size:8px;line-height:9px;padding-top:5px}
.badge strong{display:block;font-size:17px;line-height:16px}
.event span{position:absolute;left:53px;font-size:11.5px;font-weight:600;line-height:12.5px;white-space:nowrap}

.site-footer{position:absolute;left:0;top:1072px;width:959px;height:128px;background:var(--teal);color:#fff}
.f-col{position:absolute;top:17px;font-size:10.5px;line-height:13px}
.newsletter h4{position:absolute;left:600px;top:12px;font-family:"Oswald",sans-serif;font-weight:400;font-size:15px}
.newsletter .field{position:absolute;left:601px;top:35px;width:158px;height:18px;background:#fff;color:#333;font-size:9.5px;line-height:18px;padding-left:6px}
.newsletter .go{position:absolute;left:759px;top:35px;width:71px;height:18px;background:var(--orange);font-size:10.5px;font-weight:700;text-align:center;line-height:18px}
.f-rule{position:absolute;left:135px;top:68px;width:712px;height:1px;background:rgba(255,255,255,.25)}
.f-nav{position:absolute;left:0;top:79px;width:959px;display:flex;justify-content:center;gap:17px;font-size:10px;font-weight:600}
.copy{position:absolute;left:0;top:102px;width:959px;text-align:center;font-size:10px}
</style>
</head>
<body>

<header class="site-header">
  <div class="brand"><span class="brand-dot"></span><span>Lou Benfield<br>Tennis Academy</span></div>
  <nav class="top-links"><span>Home</span><span>Conatct Us</span></nav>
  <span class="social" style="left:747px"></span>
  <span class="social" style="left:780px"></span>
  <span class="social" style="left:813px"></span>

  <nav class="main-nav">
    <ul>
      <li style="width:89px">Programs</li>
      <li style="width:105px">Competitions</li>
      <li style="width:89px">Court Hire</li>
      <li style="width:84px">Restrings</li>
      <li style="width:67px">Gallery</li>
      <li style="width:86px">Schedule</li>
      <li style="width:59px">Blog</li>
      <li style="width:63px">About</li>
      <li style="width:63px">News</li>
    </ul>
  </nav>
</header>

<section class="hero" role="img" aria-label="Photo of a young boy hitting a forehand on a green tennis court, with a dark windbreak fence and hedge behind him"></section>
<aside class="who">
  <h2>Who we are</h2>
  <p>Lorem Ipsum. Proin gravida nibh vel velit auctor aliquet. Aenean sollicitudin, lorem quis bibendum auctor, nisi elit consequat ipsum, nec sagittis sem nibh id elit. Duis sed odio sit amet nibh vulputate cursus a sit amet mauris.</p>
</aside>
<div class="who-arrows">
  <div style="background:var(--yellow)"><svg width="24" height="8" viewBox="0 0 24 8"><path d="M23 4H2M5 1L2 4l3 3" stroke="#fff" fill="none" stroke-width="1.2"/></svg></div>
  <div style="background:var(--orange)"><svg width="24" height="8" viewBox="0 0 24 8"><path d="M1 4h21M19 1l3 3-3 3" stroke="#fff" fill="none" stroke-width="1.2"/></svg></div>
</div>

<section class="camp-banner">
  <div class="camp-photo" role="img" aria-label="Photo of a small child swinging a tennis racquet at a ball"></div>
  <div class="dash"></div>
  <div class="camp-title">Summer Holiday Camps</div>
  <div class="camp-sub">Secure your childs place!</div>
  <div class="book-btn">BOOK ONLINE NOW</div>
</section>
<div class="dots"><span></span><span></span><span></span><span></span><span></span></div>

<section class="widgets">
  <article class="card" style="left:127px">
    <div class="card-title">Player of the Month</div>
    <div class="player-photo" role="img" aria-label="Photo of the player of the month with a coach and teammate"></div>
    <div class="player-name">Sam Whitford June 2013</div>
    <div class="learn">LEARN MORE</div>
  </article>

  <article class="card" style="left:367px">
    <div class="card-title">Recent Post</div>
    <div class="post" style="top:61px">
      <h3>Rain Make Ups Term 3-2013</h3>
      <div class="meta">Posted by <b>marcus</b> - Aug 15, 2013</div>
      <div class="thumb" role="img" aria-label="Rain cloud illustration"></div>
      <p>Thursday Hot Shots – Sunday 18th August @ 2pm. Friday Junior Elite – Sunday 18th August @ 3pm. <b>Read more...</b></p>
    </div>
    <div class="post" style="top:162px">
      <h3>Holler for a Hoodie Winners</h3>
      <div class="meta">Posted by <b>marcus</b> - Aug 1, 2013</div>
      <div class="thumb" role="img" aria-label="Photo of an academy hoodie"></div>
      <p>We have a gone a little crazy and have selected 9 winners (instead of just 3) who will all receive a free. <b>Read more...</b></p>
    </div>
    <div class="learn">LEARN MORE</div>
  </article>

  <article class="card" style="left:607px">
    <div class="card-title">Upcoming Events</div>
    <div class="event" style="top:61px"><div class="badge"><small>AUG</small><strong>26</strong></div><span style="top:15px">City Open 2013</span></div>
    <div class="event" style="top:128px"><div class="badge"><small>SEP</small><strong>08</strong></div><span style="top:2px">8:00 AM RDTA Comp<br>T3-2013 @ LBTA Northgate<br>(Home Matches)</span></div>
    <div class="event" style="top:194px;border:none"><div class="badge"><small>SEP</small><strong>15</strong></div><span style="top:2px">8:00 AM RDTA Comp<br>T3-2013 @ LBTA Northgate<br>(Home Matches)</span></div>
    <div class="learn">LEARN MORE</div>
  </article>
</section>

<footer class="site-footer">
  <svg class="abs" style="left:120px;top:18px" width="10" height="13" viewBox="0 0 10 13"><path d="M5 0a5 5 0 0 1 5 5c0 3-5 8-5 8S0 8 0 5a5 5 0 0 1 5-5z" fill="#d6f0f3"/><circle cx="5" cy="5" r="2" fill="#2ea6b3"/></svg>
  <div class="f-col" style="left:136px"><b>LBTA PTY LTD</b><br>48 Carrow Lane,<br>Northgate NSW 2190.</div>
  <svg class="abs" style="left:286px;top:18px" width="8" height="13" viewBox="0 0 8 13"><path d="M2 0h3l-1 3-2 1c0 2 1 4 2 5l2-1 2 2-2 3C2 12 0 8 0 4z" fill="#d6f0f3"/></svg>
  <div class="f-col" style="left:298px"><b>Phone:</b><br>+(02) 5550-1824</div>
  <svg class="abs" style="left:415px;top:19px" width="13" height="9" viewBox="0 0 13 9"><rect width="13" height="9" fill="#d6f0f3"/><path d="M0 0l6.5 5L13 0" stroke="#2ea6b3" fill="none"/></svg>
  <div class="f-col" style="left:432px"><b>Email:</b><br>info@lbta.com.au/</div>
  <div class="newsletter">
    <h4>NEWSLETTER</h4>
    <div class="field">Enter your email address</div>
    <div class="go">SUBSCRIBE</div>
  </div>
  <div class="f-rule"></div>
  <nav class="f-nav"><span>Home</span><span>Programs</span><span>Competitions</span><span>Court Hire</span><span>Restrings</span><span>Gallery</span><span>Schedule</span><span>Blog</span><span>About</span><span>News</span><span>Contact Us</span></nav>
  <div class="copy">Copyright © 2013 LBTA PTY LTD. All rights reserved.</div>
</footer>

</body>
</html>
```